Need a Poster Design A3 for our Cricket Competition

We need a poster design for our upcoming T20 cricket competition Coastline Summer Cup (CSC).

it should say like this:

Bellwick Real Estate (logo supplied)
proudly presents

Coastline Summer Cup (logo supplied)

its a T20 cricket competition

starting 1st April 2018
Registrations Closing : 18th March

prizes worth $5000 to be won

for Registration contact: 0401937265 / 0402816394 and our /coastlinesummercup..see last time's poster

and then sponsors
Updates

Hello.. We will be closing the contest earlier by 5 days so we need to get the design by Tuesday 13th Feb .. Thanks

Industry/Entity Type

Real Estate

Colors

Designer to choose colors to be used in the design.

Requirements
Must have
• emphasis on our main sponsor Bellwick Real Estate & our competition logo

```html
<!DOCTYPE html>
<html lang="en">
<head>
<meta charset="utf-8">
<title>Coastline Summer Cup – T20 Poster</title>
<link rel="stylesheet" href="https://fonts.googleapis.com/css2?family=Montserrat:wght@400;500;600;700;800;900&display=swap">
<style>
  :root {
    --page: #ffffff;
    --night: #0d1a5c;
    --sky: #2b3f9e;
    --glow: #6f8fd8;
    --grass: #3f7a2a;
    --grass-dark: #1e3d14;
    --ribbon: #d0202c;
    --ribbon-dark: #8e1119;
    --ball: #c7161f;
    --gold: #f2b321;
    --gold-deep: #b86a0a;
    --white: #ffffff;
    --panel: rgba(22, 58, 16, 0.82);
    --ink: #1c1c1c;
  }
  * { box-sizing: border-box; margin: 0; padding: 0; }
  html, body {
    width: 992px; height: 1200px; overflow: hidden;
    background: var(--page);
    font-family: "Montserrat", Arial, sans-serif;
  }
  .poster {
    position: absolute; left: 123px; top: 54px;
    width: 718px; height: 1110px; overflow: hidden;
    color: var(--white);
  }
  .stadium-backdrop {
    position: absolute; inset: 0;
    background:
      radial-gradient(ellipse 70% 12% at 50% 62%, rgba(200,220,255,0.55), transparent 70%),
      linear-gradient(180deg, var(--night) 0%, var(--sky) 30%, #1a2a78 50%, var(--glow) 60%, #233a7a 64%, var(--grass) 68%, var(--grass-dark) 100%);
  }
  .sponsor-name-main {
    position: absolute; left: 0; right: 0; top: 110px;
    text-align: center; font-weight: 500; letter-spacing: 4px;
  }
  .sponsor-name-main .line1 { display: block; font-size: 38px; line-height: 1; }
  .sponsor-name-main .line2 { display: block; font-size: 10px; letter-spacing: 3px; margin-top: 6px; }
  .presents {
    position: absolute; left: 0; right: 0; top: 172px;
    text-align: center; font-size: 22px; font-weight: 500; letter-spacing: 6px;
  }
  .event-mark {
    position: absolute; left: 112px; top: 218px; width: 510px; height: 226px;
  }
  .event-mark .ball {
    position: absolute; left: 10px; top: 14px; width: 170px; height: 170px;
    border-radius: 50%; background: var(--ball);
  }
  .event-mark .acronym {
    position: absolute; left: 205px; top: 2px; font-size: 150px; font-weight: 900;
    line-height: 1; letter-spacing: 2px;
  }
  .event-mark .full-name {
    position: absolute; left: 0; right: 0; top: 186px; text-align: center;
    font-size: 33px; font-weight: 900; letter-spacing: 1px; line-height: 1; white-space: nowrap;
  }
  .start-ribbon {
    position: absolute; left: 29px; top: 453px; width: 654px; height: 54px;
  }
  .start-ribbon svg { position: absolute; inset: 0; }
  .start-ribbon .ribbon-text {
    position: absolute; inset: 0; display: flex; align-items: center; justify-content: center;
    font-size: 35px; font-weight: 400; white-space: nowrap;
  }
  .start-ribbon strong { font-weight: 800; margin: 0 10px; }
  .prize {
    position: absolute; left: 215px; top: 512px; display: flex; align-items: flex-end; gap: 10px;
  }
  .prize .win {
    font-size: 54px; font-weight: 900; font-style: italic; line-height: 1;
    background: linear-gradient(180deg, var(--gold) 0%, #ffd966 45%, var(--gold-deep) 100%);
    -webkit-background-clip: text; background-clip: text; color: transparent;
  }
  .prize .worth { line-height: 1; }
  .prize .worth small { display: block; font-size: 16px; font-weight: 500; }
  .prize .worth b { display: block; font-size: 44px; font-weight: 800; }
  .format-badge {
    position: absolute; left: 438px; top: 568px; width: 226px; height: 150px;
    border-radius: 18px;
    background: radial-gradient(circle at 70% 60%, #d5202c, #e9a423 55%, rgba(150,20,30,0.7) 100%);
  }
  .thanks-panel {
    position: absolute; left: 24px; top: 754px; width: 666px; height: 268px;
    border-radius: 14px; background: var(--panel);
  }
  .thanks-panel h2 {
    position: absolute; left: 0; right: 0; top: 9px; text-align: center;
    font-size: 19px; font-weight: 700;
  }
  .sponsor-card {
    position: absolute; left: 0; top: 35px; width: 666px; height: 186px;
    background: var(--white); border-radius: 12px; padding: 26px 14px 14px;
    display: flex; flex-direction: column; justify-content: space-between;
  }
  .sponsor-row { display: flex; justify-content: space-between; align-items: center; }
  .sponsor {
    font-weight: 700; font-size: 11px; line-height: 1.15; text-align: center; color: var(--c, var(--ink));
  }
  .sponsor .tag { display: block; font-size: 6px; font-weight: 700; letter-spacing: .5px; }
  .sponsor.lg { font-size: 17px; }
  .register {
    position: absolute; left: 0; right: 0; top: 993px; text-align: center;
    font-size: 19px; font-weight: 700;
  }
  .register-details {
    position: absolute; left: 0; right: 0; top: 1032px; text-align: center;
  }
  .register-details .phones { display: block; font-size: 24px; font-weight: 800; letter-spacing: 1px; line-height: 1.2; }
  .register-details .notes { display: block; font-size: 13px; font-weight: 600; margin-top: 8px; letter-spacing: .5px; }
</style>
</head>
<body>
<main class="poster">
  <div class="stadium-backdrop" role="img" aria-label="Floodlit cricket stadium at night with coloured smoke over a green outfield"></div>

  <header class="sponsor-name-main">
    <span class="line1">BELLWICK</span>
    <span class="line2">REAL ESTATE</span>
  </header>
  <p class="presents">PROUDLY PRESENTS</p>

  <section class="event-mark" aria-label="Coastline Summer Cup">
    <span class="ball"></span>
    <span class="acronym">CSC</span>
    <span class="full-name">COASTLINE SUMMER CUP</span>
  </section>

  <div class="start-ribbon">
    <svg viewBox="0 0 654 54" width="654" height="54" aria-hidden="true">
      <polygon points="0,8 60,8 60,54 10,54" fill="var(--ribbon-dark)"/>
      <polygon points="654,8 594,8 594,54 644,54" fill="var(--ribbon-dark)"/>
      <polygon points="24,0 630,0 610,54 44,54" fill="var(--ribbon)"/>
    </svg>
    <p class="ribbon-text">STARTING<strong>1ST APRIL</strong>2018</p>
  </div>

  <div class="prize">
    <span class="win">WIN!</span>
    <span class="worth"><small>PRIZES WORTH</small><b>$5000</b></span>
  </div>

  <div class="format-badge" role="img" aria-label="T20 format badge with helmet, bat, stumps and red ball"></div>

  <section class="thanks-panel">
    <h2>THANKS TO ALL OUR SPONSORS AND SUPPORTERS</h2>
    <div class="sponsor-card">
      <div class="sponsor-row">
        <span class="sponsor lg" style="--c:#f36f21">keel<span class="tag">REAL ESTATE</span></span>
        <span class="sponsor" style="--c:#2a6bb3">Brightvale Finance<span class="tag">HOME LOAN SPECIALISTS</span></span>
        <span class="sponsor lg" style="--c:#2b3f8f">NPRS</span>
        <span class="sponsor" style="--c:#2a5d8f">Gatefold<br>Security</span>
        <span class="sponsor" style="--c:#111">Northpole Freight</span>
        <span class="sponsor" style="--c:#c8102e">Northpole Freight</span>
      </div>
      <div class="sponsor-row">
        <span class="sponsor" style="--c:#333">Terra<span class="tag">ORGANIC COTTON</span></span>
        <span class="sponsor" style="--c:#7a2a8c">Lumen Education<span class="tag">SPREADING KNOWLEDGE</span></span>
        <span class="sponsor" style="--c:#1d3f8f">Allday Truck<span class="tag">SERVICE &amp; REPAIRS TO ALL MAKES</span></span>
        <span class="sponsor" style="--c:#c8102e">Ridgeway Motors</span>
        <span class="sponsor" style="--c:#b8860b">SAFFRA</span>
        <span class="sponsor" style="--c:#222">Marlow<span class="tag">FAMILY TRUST</span></span>
        <span class="sponsor" style="--c:#c8102e">KRT<span class="tag">LOGISTICS</span></span>
      </div>
      <div class="sponsor-row">
        <span class="sponsor" style="--c:#8a5a1c">Honeycrest<br>Sweets</span>
        <span class="sponsor" style="--c:#d0202c">Quill Express</span>
        <span class="sponsor" style="--c:#222">Vista TV</span>
        <span class="sponsor" style="--c:#e0571b">9 Lemons</span>
        <span class="sponsor" style="--c:#0b5fa5">Crustly Pizza<span class="tag">EPPING</span></span>
        <span class="sponsor" style="--c:#2b3f8f">Sparrow<span class="tag">PRINTING</span></span>
        <span class="sponsor" style="--c:#b0121b">Oakfield<span class="tag">ROADLINES</span></span>
      </div>
    </div>
  </section>

  <p class="register">FOR REGISTRATION CONTACT:</p>
  <p class="register-details">
    <span class="phones">0401937265 / 0402816394</span>
    <span class="notes">REGISTRATIONS CLOSING: 18TH MARCH &nbsp;·&nbsp; /coastlinesummercup</span>
  </p>
</main>
</body>
</html>
```